I need a book cover design for my book "Scarlet Brambles." It is a non-fiction book focused on answering the question of whether American evangelicals look more like the Pharisees than Jesus.

The subtitle is "The Quiet Parallels of Modern Suburban Townsfolk and an Ancient Kingdom's Proud Rulers." The author name is Colin Marwood.

I will be publishing this as an ebook and paperback.

I am open to all ideas, but will share the only thought I had as a possible design. In the title, the third letter in both words is "A." I thought about the idea of having the "A" in "Evangelical" have a halo and the "A" in "Pharisees" somehow seem to be a shadow of that first "A" but have devil horns instead of a halo. Again, I'm not sold on that, but am sharing it as one design possibility.

I am not interested in the book cover design having a cheesy religious look to it (as many do). I am more interested in it looking like a professional non-fiction cover.

```html
<!DOCTYPE html>
<html lang="en">
<head>
<meta charset="utf-8">
<title>Scarlet Brambles — Book Cover</title>
<link rel="stylesheet" href="https://fonts.googleapis.com/css2?family=Fraunces:opsz,wght,SOFT@9..144,700..900,100&display=swap">
<style>
  :root {
    --scarlet: #d6243f;
    --spine-red: #d3233c;
    --spine-ink: #5a0e18;
    --sky-top: #cfe6d4;
    --sky-cream: #f4ecc0;
    --sky-teal: #7fb3b2;
    --field-red: #d9505a;
    --field-glow: #f7dcae;
    --field-deep: #b8344a;
    --water: #7cc4c0;
    --water-light: #c9e6d8;
  }
  * { margin: 0; padding: 0; box-sizing: border-box; }
  html, body { width: 1200px; height: 969px; overflow: hidden; background: #ffffff; }
  .cover {
    position: relative;
    width: 1200px;
    height: 969px;
    font-family: "Fraunces", "Cooper Black", Georgia, serif;
    font-variation-settings: "SOFT" 100;
  }
  .scene {
    position: absolute;
    top: 0;
    height: 969px;
    background:
      radial-gradient(ellipse 55% 40% at 55% 55%, rgba(250,232,180,0.85), rgba(250,232,180,0) 70%),
      linear-gradient(to bottom,
        var(--sky-top) 0px,
        var(--sky-cream) 150px,
        var(--sky-teal) 205px,
        #e9c9a0 268px,
        var(--field-red) 275px,
        #e88a78 420px,
        var(--field-red) 600px,
        var(--field-deep) 770px,
        #e6b6a0 778px,
        var(--water) 800px,
        var(--water-light) 900px,
        var(--water) 969px);
  }
  .scene--back { left: 0; width: 577px; }
  .scene--front { left: 623px; width: 577px; }

  .spine {
    position: absolute;
    left: 577px;
    top: 0;
    width: 46px;
    height: 969px;
    background: var(--spine-red);
    display: flex;
    flex-direction: column;
    align-items: center;
  }
  .spine__title {
    writing-mode: vertical-rl;
    color: var(--spine-ink);
    font-weight: 900;
    font-size: 34px;
    line-height: 46px;
    margin-top: 232px;
    letter-spacing: 0.5px;
  }

  .front {
    position: absolute;
    left: 623px;
    top: 0;
    width: 577px;
    height: 969px;
    text-align: center;
    color: var(--scarlet);
  }
  .front__title {
    position: absolute;
    top: 262px;
    left: 0;
    width: 100%;
    font-weight: 900;
    font-size: 76px;
    line-height: 90px;
    letter-spacing: 0.5px;
  }
  .front__title-line { display: block; }
  .front__subtitle {
    position: absolute;
    top: 492px;
    left: 0;
    width: 100%;
    font-weight: 800;
    font-size: 20px;
    line-height: 27.3px;
  }
  .front__author {
    position: absolute;
    top: 882px;
    left: 0;
    width: 100%;
    font-weight: 900;
    font-size: 45px;
    line-height: 56px;
  }
</style>
</head>
<body>
<div class="cover">
  <div class="scene scene--back" role="img" aria-label="Dreamlike landscape: a lone red-leafed tree on a crimson field beneath a pale sky, white feathers drifting down, the tree reflected in still turquoise water"></div>
  <div class="scene scene--front" role="img" aria-label="Dreamlike landscape: a lone red-leafed tree on a crimson field beneath a pale sky with birds in flight, reflected in still turquoise water"></div>

  <div class="spine">
    <div class="spine__title">Scarlet Brambles</div>
  </div>

  <div class="front">
    <h1 class="front__title">
      <span class="front__title-line">Scarlet</span>
      <span class="front__title-line">Brambles</span>
    </h1>
    <p class="front__subtitle">
      The Quiet Parallels<br>
      of<br>
      Modern Suburban Townsfolk<br>
      and<br>
      an Ancient Kingdom's Proud Rulers.
    </p>
    <p class="front__author">Colin Marwood</p>
  </div>
</div>
</body>
</html>
```